Labels/logo for luxury bath products

I am developing a range of luxury bath foams - aimed at the top end of the luxury market. My company name is VEM (very basic website can be seen at www.vemarton.example).

I am looking for a label design for the front of the bottle, which should incorporate the VEM logo as per the website (file attached), but embedded within a more intricate label design. I provide a link to a picture of the bottle below.

The bath foam will come in four fragrances: Vetiver, Sandalwood, Jasmine and Neroli. The label should include the fragrance name. So the label must include the brand name 'VEM' and the name of the fragrance - e.g. Sandalwood Bath Foam, Neroli Bath Foam, etc.

The products are aimed at both the male and female market and so shouldn't be too feminine.

A brand to take inspiration from is Lune Bravière: http://www.lunebraviere.example/ - I like the labels that they use on their products, which is a gold embossed crest, which they use as the label for their products. I am not referring to their font, but to their label design - I like the embossed label, and am quite keen on metallics.

Conversely, I would like to add a contemporary edge to this design - I like the striping and contemporary fonts on this design: http://www.hadley-frost.example/images/fac83.jpg

My brand also harnesses the powers of natural flower ingredients, and so I am inspired by the products of Quenby - quenby.example. This labelling is more clinical and scientific.

Ideally I would like a label which combines these elements - i.e. a luxury label with a contemporary feel, that incorporate the scientific nature of the product.

The design needs to communicate high end luxury. The bottle is however apothecary style, and a nod to science and botany would be good. I would however like a bold approach to this design - it is a modern brand.

The bottle being used for the product can be seen at: http://www.tavel-vitro.example/en/product-groups/8-Apothecary-bottles - these are extremely expensive bottles and the label needs to reflect this quality. These bottles are traditional in design, but incorporate high end glassware technology to preserve the integrity of the natural ingredients. Therefore the product is a mix of old and new, and the label could also reflect this. The colour of the glass is very deep purple.

The front label does not need information such as weight/volume - it purely needs a label which will recognise it as the VEM brand, with the product name. I am looking for a high quality label, which is unique. I am happy to print embossed labels and to use foils on my labels.

Please do not be boring! I appreciate I have given a variety of influences, so summarise the requirements are a mix of:

a bold design
contemporary
luxury

The label must include NO slogans.

I am looking to build a relationship with a graphic designer for packaging and website design requirements so this will be the first of many projects.

Target Market(s)

Luxury end of market - clientele will like luxury and will pay for the highest quality ingredients in the product, but will also appreciate the botanical nature of the product.

Industry/Entity Type

Graphic Designer

Requirements
Must have
• Must include the company name, VEM, although this doesn't need to be particularly prominent. And the product name, e.g. Sandalwood.
Nice to have
• It should combine luxury, but with recognition of the science behind the product.
Should not have
• No slogans, minimal wording on the front label. No other wording other than company name and product name. No primary colours.

```html
<!DOCTYPE html>
<html lang="en">
<head>
<meta charset="utf-8">
<title>VEM Bath Foam Labels</title>
<link href="https://fonts.googleapis.com/css2?family=Montserrat:wght@700&family=Cormorant+Garamond:ital,wght@0,700;1,500&display=swap" rel="stylesheet">
<style>
  :root {
    --gold: #f2b705;
    --page: #ffffff;
    --sandalwood: #3e1350;
    --vetiver: #5a3223;
    --neroli: #b11d27;
    --jasmine: #066449;
  }
  * { box-sizing: border-box; margin: 0; padding: 0; }
  html, body {
    width: 1200px;
    height: 900px;
    overflow: hidden;
    background: var(--page);
  }
  .label-range {
    width: 1200px;
    height: 900px;
    display: flex;
    justify-content: center;
    align-items: center;
    gap: 40px;
  }
  .label {
    position: relative;
    width: 250px;
    height: 375px;
    border: 3px solid var(--gold);
    background: var(--label-colour);
  }
  .label--sandalwood { --label-colour: var(--sandalwood); }
  .label--vetiver { --label-colour: var(--vetiver); }
  .label--neroli { --label-colour: var(--neroli); }
  .label--jasmine { --label-colour: var(--jasmine); }

  .label__frame {
    position: absolute;
    inset: 5px;
    border: 2px solid var(--gold);
    display: flex;
    flex-direction: column;
  }
  .label__brand {
    height: 272px;
    border-bottom: 2px solid var(--gold);
    display: flex;
    flex-direction: column;
    align-items: center;
    padding-top: 40px;
  }
  .label__mark {
    width: 100px;
    height: 100px;
    border: 4px solid var(--gold);
  }
  .label__name {
    margin-top: 26px;
    font-family: "Montserrat", sans-serif;
    font-weight: 700;
    font-size: 50px;
    line-height: 1;
    letter-spacing: 0.01em;
    color: var(--gold);
  }
  .label__fragrance {
    flex: 1;
    display: flex;
    flex-direction: column;
    align-items: center;
    justify-content: center;
    padding-bottom: 4px;
    color: var(--gold);
  }
  .label__scent {
    font-family: "Cormorant Garamond", serif;
    font-weight: 700;
    font-size: 19px;
    letter-spacing: 0.2em;
    text-transform: uppercase;
    line-height: 1.1;
  }
  .label__botanical {
    margin-top: 5px;
    font-family: "Cormorant Garamond", serif;
    font-style: italic;
    font-weight: 500;
    font-size: 13.5px;
    line-height: 1.1;
  }
</style>
</head>
<body>
  <main class="label-range">
    <article class="label label--sandalwood">
      <div class="label__frame">
        <div class="label__brand">
          <div class="label__mark"></div>
          <p class="label__name">VEM</p>
        </div>
        <div class="label__fragrance">
          <h2 class="label__scent">Sandalwood</h2>
          <p class="label__botanical">Santalum album</p>
        </div>
      </div>
    </article>

    <article class="label label--vetiver">
      <div class="label__frame">
        <div class="label__brand">
          <div class="label__mark"></div>
          <p class="label__name">VEM</p>
        </div>
        <div class="label__fragrance">
          <h2 class="label__scent">Vetiver</h2>
          <p class="label__botanical">Vetiveria Zizanoid</p>
        </div>
      </div>
    </article>

    <article class="label label--neroli">
      <div class="label__frame">
        <div class="label__brand">
          <div class="label__mark"></div>
          <p class="label__name">VEM</p>
        </div>
        <div class="label__fragrance">
          <h2 class="label__scent">Neroli</h2>
          <p class="label__botanical">Citrus aurantium</p>
        </div>
      </div>
    </article>

    <article class="label label--jasmine">
      <div class="label__frame">
        <div class="label__brand">
          <div class="label__mark"></div>
          <p class="label__name">VEM</p>
        </div>
        <div class="label__fragrance">
          <h2 class="label__scent">Jasmine</h2>
          <p class="label__botanical">Jasminum grandiflorum</p>
        </div>
      </div>
    </article>
  </main>
</body>
</html>
```